Healthy snack food company needs a package design

We need a package design for a dry roasted flax seed snack. Consumers are not familiar with the concept of eating seasoned roasted flax as an on-the-go snack, so we want to break the image of flax being only used as an ingredient. It is very important to capture the idea of pouring the flax seeds into a hand and consuming directly. This product will compete with other nuts, chips, snack items in stores. Our seeds are crunchy and flavored with Chili Lime Seasoning to make them an irresistible snack, that also happens to be extremely good for you. This product will come in a 5oz stand up pouch bag with zip closure and peg hook hole at the top.

Target Market(s)

Individuals and families of all age groups seeking a healthy snacking option

Industry/Entity Type

Consumer

Font styles to use
Sans Serif

Requirements
Must have
• - Image/sketch of roasted flax seed in an appetizing/creative manner that conveys on the go snacking. Product to be eaten by hand, so a graphic illustration/sketch showing the flax seeds being poured in hand and eaten (pour - enjoy - repeat) for example
• - Product callouts: “Roasted Flax Seed”; “Read-To-Eat Snack” “Chili Lime” flavor
• - Company Name: Tovela (we are not providing the logo because we don’t want that to influence the package design)
Nice to have
• - Creative identity: Premium, Fun
• -Product claims include Organic, Non-GMO, High in fiber, protein, omega-3, iron. These don’t need to be called out, just sharing if desired to incorporate
Should not have
• No see through window

```html
<!DOCTYPE html>
<html lang="en">
<head>
<meta charset="utf-8">
<title>Tovela Roasted Flaxseed Pouch</title>
<link href="https://fonts.googleapis.com/css2?family=Roboto+Condensed:ital,wght@0,400;0,700;1,800&family=Poppins:ital,wght@1,800&display=swap" rel="stylesheet">
<style>
  :root {
    --backdrop: #e6dccd;
    --gold-light: #f1d499;
    --gold: #dcb46c;
    --gold-deep: #c79a4f;
    --navy: #143a52;
    --navy-deep: #0f2e44;
    --cream: #f6ebd3;
    --accent-gold: #f2c65a;
    --label-gold: #e0a84a;
    --ink: #3a2d20;
    --white: #f7f5f0;
  }
  * { margin: 0; padding: 0; box-sizing: border-box; }
  html, body { width: 1200px; height: 975px; overflow: hidden; }
  body { background: var(--backdrop); position: relative; font-family: "Roboto Condensed", sans-serif; }

  .pouch { position: absolute; left: 360px; top: 68px; width: 480px; height: 840px; }
  .pouch-art { position: absolute; inset: 0; width: 480px; height: 840px; }

  .reseal-note {
    position: absolute; right: 22px; top: 52px;
    font-family: "Roboto Condensed", sans-serif; font-weight: 400;
    font-size: 13px; letter-spacing: 0.3px; color: var(--ink);
  }

  .brand {
    position: absolute; left: 50%; top: 162px; transform: translateX(-50%);
    width: 78px; height: 78px; border-radius: 50%;
    border: 1.5px solid rgba(247,245,240,0.35);
    display: flex; align-items: center; justify-content: center;
  }
  .brand-name {
    font-family: "Roboto Condensed", sans-serif; font-weight: 700;
    font-size: 15px; color: rgba(247,245,240,0.6); letter-spacing: 0.5px;
  }

  .product-title {
    position: absolute; left: 0; right: 0; top: 262px; text-align: center;
    font-family: "Roboto Condensed", sans-serif; font-weight: 700;
    font-size: 54px; line-height: 1; color: var(--white); letter-spacing: -0.5px;
  }
  .flavour {
    position: absolute; left: 0; right: 0; top: 328px; text-align: center;
    font-family: "Poppins", sans-serif; font-style: italic; font-weight: 800;
    font-size: 24px; letter-spacing: -0.5px; color: var(--accent-gold);
  }
  .claims {
    position: absolute; left: 0; right: 0; top: 377px; text-align: center;
    font-family: "Roboto Condensed", sans-serif; font-weight: 400;
    font-size: 12.5px; color: var(--accent-gold);
  }
  .snack-callout {
    position: absolute; left: 160px; top: 476px; transform: rotate(-5deg);
    font-family: "Poppins", sans-serif; font-style: italic; font-weight: 800;
    font-size: 23px; letter-spacing: -0.3px; color: var(--label-gold);
  }
</style>
</head>
<body>
  <div class="pouch">
    <svg class="pouch-art" viewBox="0 0 480 840" xmlns="http://www.w3.org/2000/svg">
      <defs>
        <linearGradient id="foil" x1="0" y1="0" x2="1" y2="0">
          <stop offset="0" stop-color="#e8c37e"/>
          <stop offset="0.5" stop-color="#f3d9a2"/>
          <stop offset="1" stop-color="#ddb46c"/>
        </linearGradient>
        <linearGradient id="navyband" x1="0" y1="0" x2="1" y2="1">
          <stop offset="0" stop-color="#163f58"/>
          <stop offset="1" stop-color="#0f2e44"/>
        </linearGradient>
        <linearGradient id="hands" x1="0" y1="0" x2="0" y2="1">
          <stop offset="0" stop-color="#f4dcc0"/>
          <stop offset="0.5" stop-color="#b97a45"/>
          <stop offset="1" stop-color="#e8c4a2"/>
        </linearGradient>
        <clipPath id="bag">
          <path d="M4 8 Q4 0 14 0 L466 0 Q476 0 476 8 L476 30 L471 34 L476 38 L478 830 Q478 840 468 840 L16 840 Q6 840 6 830 L4 38 L9 34 L4 30 Z"/>
        </clipPath>
      </defs>
      <g clip-path="url(#bag)">
        <rect class="foil-body" width="480" height="840" fill="url(#foil)"/>
        <line class="zip-line" x1="0" y1="76" x2="480" y2="76" stroke="#8a6a3a" stroke-width="1" stroke-dasharray="5 3" opacity="0.6"/>
        <path class="navy-band" d="M0 166 C120 160 300 70 480 117 L480 455 C400 470 260 470 0 500 Z" fill="url(#navyband)"/>
        <path class="cream-wave" d="M0 500 C260 470 400 470 480 455 L480 500 C380 510 250 540 0 560 Z" fill="var(--cream)"/>
        <rect class="hand-photo" x="30" y="555" width="420" height="285" rx="0" fill="url(#hands)" opacity="0.85" role="img" aria-label="Photo of two cupped hands holding roasted flax seeds shaped like a heart"/>
      </g>
    </svg>

    <span class="reseal-note">RESEALABLE BAG</span>

    <div class="brand"><span class="brand-name">Tovela</span></div>

    <h1 class="product-title">ROASTED FLAXSEED</h1>
    <p class="flavour">CHILI LIME FLAVOURED</p>
    <p class="claims">ORGANIC, NON-GMO, HIGH IN FIBER, RICH IN PROTEIN, OMEGA-3-IRON</p>

    <p class="snack-callout">READY TO EAT SNACK</p>
  </div>
</body>
</html>
```